Business Card Design

New business card design

Target Market(s)

Residential & Commercial Property Managers

Industry/Entity Type

Plumbing Services

Contact Information for Business Card

Name - Owen Tredgold, title - Director, Phone Number - 0431 862 507, email - owen@rvb-plumbing.com.au, Company ABN - 73 215 904 386,

Font styles to use
Sans Serif

Colors
0054AA
0677BA
7BADD7
CADEEF
E8F1F8

```html
<!DOCTYPE html>
<html lang="en">
<head>
<meta charset="utf-8">
<title>RVB Plumbing Services – Business Card</title>
<link href="https://fonts.googleapis.com/css2?family=Poppins:wght@300;400;500;600&display=swap" rel="stylesheet">
<style>
  :root {
    --stage: #7c7f80;
    --blue-deep: #0054AA;
    --blue-mid: #0677BA;
    --blue-soft: #7BADD7;
    --blue-pale: #CADEEF;
    --blue-mist: #E8F1F8;
    --ink: #1c2126;
    --white: #ffffff;
  }
  * { box-sizing: border-box; margin: 0; padding: 0; }
  html, body {
    width: 1200px; height: 560px; overflow: hidden;
    background: var(--stage);
    font-family: "Poppins", sans-serif;
  }
  .stage {
    width: 1200px; height: 560px;
    display: flex; align-items: center; justify-content: center; gap: 40px;
  }
  .card {
    position: relative;
    width: 320px; height: 495px;
    box-shadow: 0 6px 10px rgba(0,0,0,0.25);
    overflow: hidden;
  }
  /* Front */
  .card-front {
    background: var(--blue-mist);
  }
  .front-mark {
    position: absolute; left: 50%; top: 50%;
    transform: translate(-50%, -50%) rotate(-90deg);
    display: flex; flex-direction: column; align-items: center;
    width: 360px;
  }
  .brand-row { display: flex; align-items: center; gap: 8px; }
  .brand-name {
    font-weight: 300; letter-spacing: 2px; line-height: 1;
  }
  .brand-dot { border-radius: 50%; background: var(--blue-mid); }
  .front-mark .brand-name { font-size: 82px; color: var(--ink); }
  .front-mark .brand-dot { width: 14px; height: 14px; margin-top: 30px; }
  .tagline {
    font-weight: 400; text-transform: lowercase; white-space: nowrap;
  }
  .front-mark .tagline {
    font-size: 10px; letter-spacing: 9px; color: var(--ink); margin-top: 10px;
  }
  /* Back */
  .card-back {
    background: var(--blue-deep);
    border-radius: 14px;
    color: var(--white);
    text-align: center;
  }
  .back-logo {
    position: absolute; top: 42px; left: 0; right: 0;
    display: flex; flex-direction: column; align-items: center;
  }
  .back-logo .brand-name { font-size: 58px; color: var(--white); }
  .back-logo .brand-dot { width: 11px; height: 11px; background: var(--blue-soft); margin-top: 22px; }
  .back-logo .tagline { font-size: 8px; letter-spacing: 7px; margin-top: 12px; }
  .divider {
    position: absolute; top: 134px; left: 27px; right: 27px;
    height: 2px; background: var(--blue-pale);
  }
  .identity { position: absolute; top: 210px; left: 0; right: 0; }
  .person-name { font-size: 30px; font-weight: 600; line-height: 1.1; }
  .person-role {
    font-size: 23px; font-weight: 400; color: var(--blue-pale);
    margin-top: 2px; padding-left: 18px; text-align: left;
  }
  .abn { font-size: 11.5px; color: var(--white); font-weight: 500; }
  .contact { position: absolute; top: 372px; left: 0; right: 0; }
  .contact-title { font-size: 16px; font-weight: 600; letter-spacing: 0.5px; margin-bottom: 12px; }
  .contact-line { font-size: 14px; font-weight: 400; line-height: 1.3; color: var(--blue-mist); }
</style>
</head>
<body>
  <main class="stage">
    <section class="card card-front" aria-label="Business card front">
      <div class="front-mark">
        <div class="brand-row">
          <span class="brand-name">rvb</span>
          <span class="brand-dot"></span>
        </div>
        <div class="tagline">plumbing services</div>
      </div>
    </section>

    <section class="card card-back" aria-label="Business card back">
      <div class="back-logo">
        <div class="brand-row">
          <span class="brand-name">rvb</span>
          <span class="brand-dot"></span>
        </div>
        <div class="tagline">plumbing services</div>
      </div>
      <div class="divider"></div>
      <div class="identity">
        <div class="person-name">OWEN Tredgold</div>
        <div class="person-role">Director <span class="abn">ABN - 73 215 904 386</span></div>
      </div>
      <div class="contact">
        <div class="contact-title">CONTACT</div>
        <div class="contact-line">Phone Number - 0431 862 507</div>
        <div class="contact-line">email - owen@rvb-plumbing.com.au</div>
      </div>
    </section>
  </main>
</body>
</html>
```